New Business Card Design Project

I have a logo I would like to use on the business card. I want something that will stand out and that will be remembered.

Target Market(s)

People who collect gems, minerals and crystals.

Contact Information for Business Card

email - mkthestonefalcon@vendrollo.com
phone # 917-406-2581

Font styles to use
Serif
Sans Serif
Decorative

Colors

Designer to choose colors to be used in the design.

Requirements
Must have
• The logo...two to choose from.
Nice to have
• An eye catching and memorable way to draw in people who collect gems minerals and crystals.

```html
<!DOCTYPE html>
<html lang="en">
<head>
<meta charset="utf-8">
<title>The Stone Falcon – Business Card</title>
<link rel="stylesheet" href="https://fonts.googleapis.com/css2?family=Mulish:wght@400;800&display=swap">
<style>
  :root {
    --backdrop: #e6e4e1;
    --card: #f7f7f6;
    --ink: #1b1b1b;
    --accent: #3d4fb8;
    --rule: #1f1f1f;
    --watermark-light: #ececec;
    --watermark-dark: #d3d3d3;
    --text: #3a3a3a;
  }
  html, body {
    margin: 0;
    width: 1200px;
    height: 960px;
    overflow: hidden;
    background: var(--backdrop);
    font-family: "Mulish", sans-serif;
  }
  .business-card {
    position: absolute;
    left: 80px;
    top: 180px;
    width: 1040px;
    height: 600px;
    background: var(--card);
    box-shadow: 0 10px 30px rgba(0,0,0,0.15);
    overflow: hidden;
  }
  .mascot-watermark {
    position: absolute;
    left: 60px;
    top: 30px;
    width: 360px;
    height: 560px;
    border-radius: 180px 180px 60px 60px;
    background: radial-gradient(ellipse at 50% 40%, var(--watermark-dark), var(--watermark-light) 75%, transparent);
    opacity: 0.7;
  }
  .brand {
    position: absolute;
    right: 60px;
    top: 150px;
    display: flex;
    align-items: center;
    gap: 14px;
  }
  .brand-dot {
    width: 22px;
    height: 22px;
    border-radius: 50%;
    background: var(--accent);
  }
  .brand-name {
    font-weight: 800;
    font-size: 40px;
    color: var(--ink);
    letter-spacing: 0.5px;
  }
  .rule {
    position: absolute;
    height: 3px;
    background: var(--rule);
  }
  .rule-main { left: 60px; right: 50px; top: 345px; }
  .rule-short { left: 60px; width: 300px; top: 412px; }
  .person-name {
    position: absolute;
    left: 60px;
    top: 282px;
    margin: 0;
    font-weight: 800;
    font-size: 48px;
    color: var(--ink);
  }
  .person-title {
    position: absolute;
    left: 62px;
    top: 360px;
    margin: 0;
    font-size: 30px;
    color: var(--accent);
  }
  .contact {
    position: absolute;
    left: 120px;
    top: 450px;
    margin: 0;
    font-size: 28px;
    line-height: 42px;
    color: var(--text);
  }
  .address {
    position: absolute;
    left: 660px;
    top: 400px;
    display: flex;
    gap: 18px;
    align-items: flex-start;
  }
  .address-lines {
    font-size: 30px;
    line-height: 42px;
    color: var(--text);
    margin: 0;
  }
  .pin-icon { margin-top: 10px; }
</style>
</head>
<body>
  <section class="business-card">
    <div class="mascot-watermark" role="img" aria-label="Faint large mascot illustration holding crystals with crossed pickaxes"></div>

    <div class="brand">
      <span class="brand-dot"></span>
      <span class="brand-name">The Stone Falcon</span>
    </div>

    <h1 class="person-name">Your Name</h1>
    <div class="rule rule-main"></div>
    <p class="person-title">Your Title</p>
    <div class="rule rule-short"></div>

    <p class="contact">917-406-2581<br>mkthestonefalcon@vendrollo.com</p>

    <div class="address">
      <svg class="pin-icon" width="24" height="34" viewBox="0 0 24 34" aria-hidden="true">
        <path d="M12 0C5.4 0 0 5.3 0 11.9 0 20.8 12 34 12 34s12-13.2 12-22.1C24 5.3 18.6 0 12 0z" fill="var(--accent)"/>
        <circle cx="12" cy="12" r="4.5" fill="var(--card)"/>
      </svg>
      <p class="address-lines">Your address<br>city, state, ZIP 0000</p>
    </div>
  </section>
</body>
</html>
```